Torvane Staffing - Mission Poster Design

We are a staffing and recruiting firm with multiple locations across the US. I am seeking a clean modern design highlighting our Mission Statement: Torvane Staffing...Linking Bright Talent with Bold Employers! This design will be framed and placed at the entrance of all of our offices. My website is www.torvanestaffing.example

Target Market(s)

Will be our company mission with a poster prominently placed in each office.

Industry/Entity Type

Staffing

Requirements
Must have
• Must be professional, clean and eye catching. We want to embrace diversity, so we like a variety of people if people will be a focal part.

```html
<!DOCTYPE html>
<html lang="en">
<head>
<meta charset="utf-8">
<title>Torvane Staffing – Mission Poster</title>
<link rel="stylesheet" href="https://fonts.googleapis.com/css2?family=Bebas+Neue&family=Montserrat:wght@700&display=swap">
<style>
  :root {
    --backdrop: #eeeeec;
    --navy: #0b0d4d;
    --navy-deep: #080a3e;
    --gold: #f2c31b;
    --red: #e8322b;
    --white: #ffffff;
    --ink: #0b0d4d;
  }
  * { margin: 0; padding: 0; box-sizing: border-box; }
  html, body {
    width: 1200px;
    height: 1200px;
    overflow: hidden;
    background: var(--backdrop);
  }
  .poster {
    position: absolute;
    left: 195px;
    top: 60px;
    width: 810px;
    height: 1080px;
    background: linear-gradient(160deg, var(--navy) 0%, var(--navy-deep) 100%);
    font-family: "Bebas Neue", "Oswald", sans-serif;
  }
  .mission-line {
    position: absolute;
    left: 64px;
    line-height: 1;
    white-space: nowrap;
    letter-spacing: 0.5px;
  }
  .mission-line--lead   { top: 64px;  font-size: 112px; color: var(--white); }
  .mission-line--bright { top: 140px; font-size: 286px; color: var(--gold); }
  .mission-line--talent { top: 364px; font-size: 286px; color: var(--gold); }
  .mission-line--with   { top: 604px; font-size: 180px; color: var(--red); }
  .mission-line--close  { top: 776px; font-size: 112px; color: var(--white); }

  .web-pill {
    position: absolute;
    left: 72px;
    top: 952px;
    width: 384px;
    height: 48px;
    border-radius: 24px;
    background: var(--gold);
    color: var(--ink);
    font-family: "Montserrat", "Arial", sans-serif;
    font-weight: 700;
    font-size: 19px;
    display: flex;
    align-items: center;
    justify-content: center;
    letter-spacing: 0.3px;
  }
  .brand {
    position: absolute;
    right: 70px;
    top: 950px;
    display: flex;
    align-items: center;
    gap: 10px;
    color: var(--white);
    font-size: 40px;
    line-height: 1;
    letter-spacing: 1px;
  }
  .brand-dot {
    width: 14px;
    height: 14px;
    border-radius: 50%;
    background: var(--red);
  }
</style>
</head>
<body>
  <main class="poster">
    <h1 class="mission">
      <span class="mission-line mission-line--lead">LINKING</span>
      <span class="mission-line mission-line--bright">BRIGHT</span>
      <span class="mission-line mission-line--talent">TALENT</span>
      <span class="mission-line mission-line--with">WITH BOLD</span>
      <span class="mission-line mission-line--close">EMPLOYERS!</span>
    </h1>
    <div class="web-pill">www.torvanestaffing.example</div>
    <div class="brand"><span class="brand-dot"></span>Torvane Staffing</div>
  </main>
</body>
</html>
```